Law Firm Needs a new Website Design

We need a new website design for our law firm located in Manhattan (Law Offices of Branford T. Quellsworth, PLLC).
We have an existing logo that we will to continue using, which can be found in www.QuellsworthLaw.example.
The Peak Counsel, Prime Advocates Logo should also be reflected near the bottom of the Home page.
The website will be 6 pages.

Deliverables:
I want a
1) home page,
2) About Us/Practice Areas page,
3) attorneys,
4) News and Articles page, and
5) Contact and Directions/Privacy Policy page.

The colors of my logo should be in the website.
I also like a touch of black and red.

The website should project "excellence."
We seek to provide the highest quality legal services.
We handle estate planning, wills, trusts, planning for people with disabilities, asset protection and preservation, Medicaid planning, hospital safe discharge, nursing home placement, powers of attorney, health care proxies, living wills, guardianships, probate, estate administration and related litigation.

I would like the colors of my Logo used (including shading where appropriate).
I also want some black on the borders and/or bottom and some red touches throughout the page.

My Logo should appear everywhere that "Law Offices Of Branford T. Quellsworth, PLLC" appears.
I want the badges for Peak counsel, Prime Advocates, Prime Legal Houses, and ZELK on the Home page.
I do not want too much text on the home page.

We would also like the website to have coding.
The final design should also communicate quality, expertise and stability.
Great start so far by the people who submitted designs.
Thank you.

Industry/Entity Type

Law Firm

Coding

Coded - Design and coding required

Number of Pages Required

5+ page

Colors
3276b5
ec1f27
474747

Requirements
Must have
• Please use my logo each time you mention Law Offices of Branford T. Quellsworth, PLLC. Please include the Peakcounsel, Prime Advocates, Prime Legal Houses and Zelk rating Badges on the web home page. I only wish to be contacted by phone. I am not including testimonials and am only using the New York City address.
Nice to have
• Prefer illustrations to photos regarding practice areas
Should not have
• Testimonials, contact me by email, free consultation.

```html
<!DOCTYPE html>
<html lang="en">
<head>
<meta charset="utf-8">
<title>Law Offices of Branford T. Quellsworth, PLLC</title>
<link href="https://fonts.googleapis.com/css2?family=Roboto:wght@300;400;500;700&family=Open+Sans:ital,wght@0,400;0,600;0,700;1,400;1,600&display=swap" rel="stylesheet">
<style>
:root{
  --blue:#3258a8;
  --blue-deep:#243f86;
  --blue-text:#2f5aa8;
  --red:#ec1f27;
  --ink:#333;
  --grey:#666;
  --pale:#f0f0f0;
  --footer:#222;
  --footer-bottom:#131313;
  --white:#fff;
}
*{box-sizing:border-box;margin:0;padding:0}
html,body{width:1200px;height:3125px;overflow:hidden}
body{font-family:"Open Sans",sans-serif;color:var(--ink);background:var(--white);position:relative}
a{color:inherit;text-decoration:none}
.site-header{height:125px;display:flex;align-items:center;padding:0 100px;justify-content:space-between}
.brand{display:flex;align-items:center;gap:14px}
.brand-mark{width:34px;height:34px;background:var(--blue-deep)}
.brand-name{font-family:"Roboto",sans-serif;font-size:19px;font-weight:500;color:var(--blue-deep);line-height:1.2;width:330px}
.header-contact{display:flex;align-items:center;gap:26px}
.header-contact .lines{font-size:15px;color:var(--grey);line-height:1.7;display:flex;gap:14px;align-items:center}
.social{display:flex;gap:6px}
.social span{width:22px;height:22px;border-radius:50%;background:var(--blue)}
.social span:nth-child(3){background:var(--red)}
.social span:nth-child(4){background:#9a9a9a}
.main-nav{height:54px;background:linear-gradient(#3556ad,#2a4593);padding:0 100px;display:flex;border-bottom:3px solid var(--red)}
.main-nav a{font-family:"Roboto",sans-serif;font-size:14px;font-weight:500;color:var(--white);padding:0 22px;line-height:51px;text-transform:uppercase;letter-spacing:.3px;margin-right:25px}
.main-nav a.active{background:#223a80;box-shadow:inset 0 -3px 0 var(--red)}
.hero{position:relative;height:497px;background:linear-gradient(100deg,#2d3748 0%,#5a6a80 45%,#8fa0b5 70%,#3e4a5c 100%)}
.hero-copy{position:absolute;left:115px;top:215px;color:var(--white);width:540px}
.hero-copy h1{font-family:"Roboto",sans-serif;font-weight:400;font-size:36px;line-height:1.15;text-transform:uppercase;margin-bottom:12px;padding-left:14px;border-left:4px solid var(--red)}
.hero-copy p{font-size:15px;line-height:1.5;width:420px}
.hero-arrow{position:absolute;top:392px;width:34px;height:34px;border-radius:50%;background:rgba(0,0,0,.55);display:flex;align-items:center;justify-content:center}
.hero-arrow.prev{left:34px}.hero-arrow.next{right:34px;background:rgba(255,255,255,.7)}
.welcome{height:415px;display:flex;padding:67px 100px 0;gap:31px}
.welcome-photo{width:431px;height:289px;border:6px solid #e8e8e8;background:linear-gradient(120deg,#2b3347,#c6cdd6 55%,#eef0f2)}
.welcome-text{width:538px;padding-top:20px}
.welcome-text h2{font-family:"Roboto",sans-serif;font-weight:400;font-size:24px;color:var(--blue-deep);line-height:1.3;text-transform:uppercase;margin-bottom:22px}
.welcome-text p{font-size:11.5px;line-height:1.78;color:var(--grey);margin-bottom:12px}
.section-title{font-family:"Roboto",sans-serif;font-weight:400;font-size:30px;color:var(--blue-text);text-align:center;text-transform:uppercase}
.divider{display:flex;align-items:center;justify-content:center;gap:10px;margin:12px 0 0}
.divider i{width:70px;height:1px;background:#bfc6d6}
.divider b{width:10px;height:10px;transform:rotate(45deg);background:var(--red)}
.practice{background:var(--pale);height:479px;padding-top:55px}
.practice-intro{font-size:12.5px;color:var(--grey);text-align:center;width:1000px;margin:16px auto 0;line-height:1.75}
.practice-grid{display:flex;justify-content:center;margin-top:36px}
.practice-item{width:260px;text-align:center}
.practice-icon{width:130px;height:130px;margin:0 auto}
.practice-item h3{font-family:"Roboto",sans-serif;font-weight:400;font-size:16px;text-transform:uppercase;margin:14px 0 8px;color:#222}
.practice-item p{font-size:12px;line-height:1.7;color:var(--grey);width:215px;margin:0 auto}
.column-band{height:285px;background:linear-gradient(#2c4889,#30508f)}
.news{height:444px;padding-top:65px}
.news-grid{display:flex;justify-content:space-between;width:1000px;margin:44px auto 0}
.news-item{width:312px}
.news-item h3{font-family:"Roboto",sans-serif;font-weight:400;font-size:15px;line-height:1.75;color:var(--blue-text);text-transform:uppercase}
.news-item a{display:inline-block;font-size:13px;color:var(--red);text-decoration:underline;margin-top:18px}
.news-button{display:block;width:196px;height:45px;margin:50px auto 0;border:2px solid var(--blue-text);color:var(--blue-text);font-family:"Roboto",sans-serif;font-size:14px;line-height:41px;text-align:center;text-transform:uppercase}
.help{height:329px;background:linear-gradient(#3a5aa8,#3658a6);color:var(--white);text-align:center;padding-top:44px}
.help-dot{width:64px;height:64px;border-radius:50%;border:3px solid rgba(255,255,255,.85);margin:0 auto;display:flex;align-items:center;justify-content:center}
.help h2{font-family:"Roboto",sans-serif;font-weight:400;font-size:26px;margin:28px 0 14px;text-transform:uppercase}
.help p{font-size:13px;line-height:1.85}
.help .phone{font-size:22px;margin-top:24px;font-family:"Roboto",sans-serif;font-weight:500}
.badges{height:161px;display:flex;align-items:center;justify-content:center;gap:60px}
.badge.tall{width:100px;height:104px;border-radius:4px;background:#c8323a}
.badge.wide{width:236px;height:58px;border-radius:6px;background:#c9a24a}
.badge.mid{width:272px;height:50px;background:#2f5aa8}
.badge.short{width:188px;height:66px;background:#1e1e1e;border-radius:4px}
.site-footer{height:274px;background:var(--footer);color:#ddd;display:flex;padding:52px 0 0 100px;border-top:4px solid var(--red)}
.footer-brand{width:254px;padding-top:30px;font-family:"Roboto",sans-serif;font-size:16px;font-weight:500;color:var(--white);line-height:1.35}
.footer-col{width:308px}
.footer-col.links{width:219px}
.footer-col h4{font-weight:600;font-size:17px;color:var(--white);text-transform:uppercase;margin-bottom:14px}
.footer-col li{list-style:none;font-size:12.5px;line-height:23.5px;text-transform:uppercase}
.footer-col address{font-style:normal;font-size:13px;line-height:1.7}
.footer-contact-row{display:flex;align-items:center;gap:10px;font-size:13px;margin-top:8px}
.footer-social{display:flex;gap:6px;margin-top:14px}
.footer-social span{width:22px;height:22px;border-radius:50%;border:1px solid #aaa}
.footer-bottom{height:59px;background:var(--footer-bottom);color:#bbb;display:flex;align-items:center;justify-content:space-between;padding:0 100px;font-size:11.5px;position:relative}
.footer-bottom .center-mark{position:absolute;left:590px;top:20px;width:20px;height:20px;background:#888}
</style>
</head>
<body>
<header class="site-header">
  <div class="brand"><span class="brand-mark"></span><span class="brand-name">Law Offices of Branford T. Quellsworth, PLLC</span></div>
  <div class="header-contact">
    <div class="lines">
      <svg width="22" height="22" viewBox="0 0 24 24"><path d="M6.6 10.8a15 15 0 0 0 6.6 6.6l2.2-2.2a1 1 0 0 1 1-.25 11 11 0 0 0 3.6.6 1 1 0 0 1 1 1V20a1 1 0 0 1-1 1A17 17 0 0 1 3 4a1 1 0 0 1 1-1h3.5a1 1 0 0 1 1 1 11 11 0 0 0 .6 3.6 1 1 0 0 1-.25 1z" fill="#bbb"/></svg>
      <div>218 HALVERN AVENUE, SUITE 1404 NEW YORK,<br>Call Us : +(212) 555-0187</div>
    </div>
    <div class="social"><span></span><span></span><span></span><span></span></div>
  </div>
</header>
<nav class="main-nav">
  <a class="active" href="#">Home</a><a href="#">Practice Areas</a><a href="#">Attorneys</a><a href="#">Privacy Policy</a><a href="#">News</a><a href="#">Contact and Directions</a>
</nav>
<section class="hero" role="img" aria-label="Photograph of brass scales of justice on a desk in a bright office">
  <div class="hero-copy">
    <h1>Law Offices of Branford T. Quellsworth</h1>
    <p>Lorem ipsum dolor sit amet, consectetur adipiscing elit, sed do eiusmod tempor incididunt ut labore et dolor sit amet.</p>
  </div>
  <span class="hero-arrow prev"><svg width="12" height="12" viewBox="0 0 12 12"><path d="M8 1 3 6l5 5" stroke="#fff" stroke-width="2" fill="none"/></svg></span>
  <span class="hero-arrow next"><svg width="12" height="12" viewBox="0 0 12 12"><path d="m4 1 5 5-5 5" stroke="#333" stroke-width="2" fill="none"/></svg></span>
</section>
<section class="welcome">
  <div class="welcome-photo" role="img" aria-label="Photograph of a hand pointing at a document beside a pen and a glass of water"></div>
  <div class="welcome-text">
    <h2>Welcome to<br>Law Offices of Branford T. Quellsworth</h2>
    <p>Our firm was founded in 1993 by Branford T. Quellsworth, a member of the National Guild of Elder Law Counsel (NGELC) and an elder law practitioner for over 19 years. Our firm is uniquely positioned to provide quality legal advice and representation in regards to estate planning, wills, trusts, planning for people with disabilities, asset protection and preservation, Medicaid planning, hospital safe discharge, nursing home placement, powers of attorney, health care proxies, living wills, guardianships, probate, estate administration and related litigation.</p>
    <p>Our familiarity with entitlement programs such as Medicaid and the statutes and regulations pertaining to them, our sensitivity to the problems and needs of seniors and our access to geriatric care managers enable us to help families preserve their life savings</p>
  </div>
</section>
<section class="practice">
  <h2 class="section-title">Our Practice Areas</h2>
  <div class="divider"><i></i><b></b><i></i></div>
  <p class="practice-intro">We are a law firm &amp; handle estate planning, wills, trusts, planning for people with disabilities, asset protection and preservation, Medicaid planning, hospital safe discharge, nursing home placement, powers of attorney, health care proxies, living wills, guardianships, probate, estate administration and related litigation</p>
  <div class="practice-grid">
    <div class="practice-item">
      <svg class="practice-icon" viewBox="0 0 130 130"><path d="M65 4 126 65 65 126 4 65z" fill="#fff" stroke="#243f86" stroke-width="6"/><path d="M65 20 110 65 65 110 20 65z" fill="#3258a8"/><rect x="52" y="48" width="26" height="34" fill="#fff"/><path d="M57 57h16M57 64h16M57 71h10" stroke="#3258a8" stroke-width="2"/></svg>
      <h3>Estate Planning</h3>
      <p>Estate planning is not just for the very wealthy or for senior citizens and often does not focus solely upon asset</p>
    </div>
    <div class="practice-item">
      <svg class="practice-icon" viewBox="0 0 130 130"><path d="M65 4 126 65 65 126 4 65z" fill="#fff" stroke="#243f86" stroke-width="6"/><path d="M65 20 110 65 65 110 20 65z" fill="#3258a8"/><circle cx="54" cy="55" r="6" fill="#fff"/><circle cx="76" cy="55" r="6" fill="#fff"/><rect x="46" y="66" width="38" height="12" rx="3" fill="#fff"/></svg>
      <h3>Probate &amp; Estate Admin</h3>
      <p>Although the family is not required to retain an attorney to handle the affairs of a deceased loved one</p>
    </div>
    <div class="practice-item">
      <svg class="practice-icon" viewBox="0 0 130 130"><path d="M65 4 126 65 65 126 4 65z" fill="#fff" stroke="#243f86" stroke-width="6"/><path d="M65 20 110 65 65 110 20 65z" fill="#3258a8"/><rect x="50" y="48" width="24" height="10" transform="rotate(-40 62 53)" fill="#fff"/><path d="M64 60 80 80" stroke="#fff" stroke-width="4"/><rect x="48" y="80" width="30" height="5" fill="#fff"/></svg>
      <h3>Powers of Attorney</h3>
      <p>Regardless of your age, it is prudent to consider what would happen if you were to become incapacitated</p>
    </div>
    <div class="practice-item">
      <svg class="practice-icon" viewBox="0 0 130 130"><path d="M65 4 126 65 65 126 4 65z" fill="#fff" stroke="#243f86" stroke-width="6"/><path d="M65 20 110 65 65 110 20 65z" fill="#3258a8"/><path d="M45 52h18l2 3 2-3h18v26H67l-2 3-2-3H45z" fill="#fff"/><path d="M65 55v23" stroke="#3258a8" stroke-width="2"/></svg>
      <h3>Needs Trusts</h3>
      <p>Eligibility for certain government benefits, such as Medicaid and Supplemental Security Income (SSI)</p>
    </div>
  </div>
</section>
<section class="column-band" role="img" aria-label="Faint photograph of a courthouse colonnade behind a blue tint"></section>
<section class="news">
  <h2 class="section-title">Latest News</h2>
  <div class="divider"><i></i><b></b><i></i></div>
  <div class="news-grid">
    <article class="news-item"><h3>Mr. Quellsworth was selected for the 2015 Prime Advocates in America in the practice of elder law</h3><a href="#">Read More</a></article>
    <article class="news-item"><h3>Mr. Quellsworth was selected for the 2015 Prime Advocates in America in the practice of elder law</h3><a href="#">Read More</a></article>
    <article class="news-item"><h3>Mr. Quellsworth was selected for the 2015 Prime Advocates in America in the practice of elder law</h3><a href="#">Read More</a></article>
  </div>
  <a class="news-button" href="#">View All News</a>
</section>
<section class="help" aria-label="Need help">
  <div class="help-dot"><svg width="26" height="26" viewBox="0 0 24 24"><path d="M6.6 10.8a15 15 0 0 0 6.6 6.6l2.2-2.2a1 1 0 0 1 1-.25 11 11 0 0 0 3.6.6 1 1 0 0 1 1 1V20a1 1 0 0 1-1 1A17 17 0 0 1 3 4a1 1 0 0 1 1-1h3.5a1 1 0 0 1 1 1 11 11 0 0 0 .6 3.6 1 1 0 0 1-.25 1z" fill="#fff"/></svg></div>
  <h2>Need Help?</h2>
  <p>Contact our customer support team if you have any further questions.<br>We are heare to help you out</p>
  <p class="phone">1-800-555-0142</p>
</section>
<section class="badges" aria-label="Rating badges">
  <div class="badge tall" role="img" aria-label="Prime Legal Houses badge"></div>
  <div class="badge wide" role="img" aria-label="Peak Counsel badge"></div>
  <div class="badge mid" role="img" aria-label="Prime Advocates badge"></div>
  <div class="badge short" role="img" aria-label="Zelk rating badge"></div>
</section>
<footer class="site-footer">
  <div class="footer-brand">Law Offices of Branford T. Quellsworth, PLLC</div>
  <div class="footer-col">
    <h4>Practice Areaslinks</h4>
    <ul><li>Medicaid Planning</li><li>Estate Planning</li><li>Probate and Estate Administration</li><li>Powers of Attorney</li><li>Supplemental Needs Trusts</li><li>Guardianships</li></ul>
  </div>
  <div class="footer-col links">
    <h4>Quick Links</h4>
    <ul><li>Home</li><li>Practice Areas</li><li>Contact and Directions</li><li>News</li><li>Privacy Policy</li><li>Attorneys</li></ul>
  </div>
  <div class="footer-col">
    <h4>Contact Us</h4>
    <address>Law Offices of Branford T. Quellsworth,<br>P.O. Box 512, Carrow Falls, NY 10990</address>
    <div class="footer-contact-row"><svg width="16" height="16" viewBox="0 0 24 24"><path d="M6.6 10.8a15 15 0 0 0 6.6 6.6l2.2-2.2a1 1 0 0 1 1-.25 11 11 0 0 0 3.6.6 1 1 0 0 1 1 1V20a1 1 0 0 1-1 1A17 17 0 0 1 3 4a1 1 0 0 1 1-1h3.5a1 1 0 0 1 1 1 11 11 0 0 0 .6 3.6 1 1 0 0 1-.25 1z" fill="#ddd"/></svg>+1 212.555.0163</div>
    <div class="footer-social"><span></span><span></span><span></span><span></span></div>
  </div>
</footer>
<div class="footer-bottom">
  <span>&copy;2014 - 2016 Law Offices of Branford T. Quellsworth, PLLC., All Rights Reserved.</span>
  <span class="center-mark"></span>
  <span>Terms of Service | Privacy Policy</span>
</div>
</body>
</html>
```